Pack Design for High Quality Marine Collagen Powder

We're looking for a quality full pack design (front and back) to sell on Brindova. We need a 2D version of front and back image in photoshop and JPG. We also need a 3D version of front and back for marketing purposes.

As many colour as needed, printing is CMYK + White digital printed.

Front of pack:

Text as follows:

Headline: 'Wild Marine Hydrolysed Collagen Powder' ...(The emphasis needs to be on the word Collagen)

Text: Essential Protein For Muscle, Hair and Skin | Rich in Amino Acids | Certified KWR Sustainably Sourced | Yeast & Gluten Free | No Additives | Unflavoured and Odorless | Water-Soluble

200g

(KWR and Sustainable logos)

Pramuvents logo at the bottom of pack. Doesn't need to be too prominent.

Back of pack:

Ingredients:
100% Pure Hydrolysed Marine Collagen (Natural)
Derived from Fish

Nutritional Information: (Please put this into a table)
Typical Values Per 10g Serving
Energy 159Kj/38kCal
Protein 9.5g
Carbohydrates 0.02g
Of which sugars 0.02g
Fat 0g
Fibre 0g
Sodium 0g
Free from GMO, Fat, Carbohydrates, Purine, Preservatives, Artificial colours/flavours
Amino Acids 99.9%
Of which essential 14.5%

This supplement should not be used as a substitute for a varied diet Do not exceed the recommended daily dose.

Please consult a healthcare practitioner if you are pregnant or taking prescription medicine before using this product.

Recommended daily dose

10-15g daily

Directions for use
Add 10g of powder to 250ml of cold water, coffee, smoothie, shake, juice, protein shake, porridge or soups.

To ensure optimum absorption, consume collagen powder at least 30 mins before a meal.

Storage information: Store in a cool dry place away from sunlight, moisture, and heat. Keep out of reach of animals and children. Keep contents dry. Reject if pack seal is broken.

Brindova Barcode image

To reorder, go to www.plinthavel.co.uk

Produced in the UK

More notes:

We have included the protein module design for inspiration of pack design along with some other designs that we like.

Pack dimensions 19cm (height) x 15cm (width). The top 2cm will be torn off by the user, so should not contain any key information.

Target Market(s)

Health conscious adults over 25

Industry/Entity Type

Marine

Colors

Designer to choose colors to be used in the design.

Requirements
Must have
• This product must stand out on Brindova and be seen. But not too busy in design and vivid enough to get clicks.
• Please only submit designs in 3D. We need a tight shadow to the right of the pack
• Final design needs to be high res ready to send to the printers with a normal bleed space around the edge.
Nice to have
• The final design should communicate quality, sustainability. The background should be clear - white ideally. Collagen is a product for health - specifically for skin and bone health.
• To help us choose, we would appreciate if you photoshop your design in 3D into an Brindova listings page - so we can see that it stands out.
Should not have
• Be too busy. Can't be bland. Text must be very readable.

```html
<!DOCTYPE html>
<html lang="en">
<head>
<meta charset="utf-8">
<title>Pramuvents Wild Marine Collagen Powder – Pack Front and Back</title>
<link rel="stylesheet" href="https://fonts.googleapis.com/css2?family=Montserrat:wght@700;800&family=Open+Sans:wght@400;600;700&family=Roboto+Condensed:wght@400;700&display=swap">
<style>
:root{
  --bg:#eceeef;
  --pack:#ffffff;
  --teal:#1f8fa3;
  --teal-dark:#0f5a68;
  --teal-light:#5cc3cf;
  --navy:#173f4a;
  --ink:#4a5558;
  --lime:#9dc43c;
  --lime-dark:#86ad2c;
  --brand:#2f9a86;
  --rule:#9aa4a7;
}
*{box-sizing:border-box;margin:0;padding:0}
html,body{width:1200px;height:846px;overflow:hidden;background:var(--bg)}
body{position:relative;font-family:"Open Sans",sans-serif;color:var(--ink)}

.pack{position:absolute;top:40px;width:510px;height:766px;background:var(--pack);overflow:hidden;box-shadow:6px 6px 14px rgba(0,0,0,.12)}
.pack--front{left:50px}
.pack--back{left:640px}

.coral-band{position:absolute;left:0;top:0;width:100%;height:110px;background:linear-gradient(180deg,#2c8f98 0%,#5bb5b6 55%,rgba(255,255,255,0) 100%)}
.wave-band{position:absolute;left:0;bottom:0;width:100%;height:52px;background:linear-gradient(180deg,#7fcfd6 0%,#1f8fa3 60%,#0f5a68 100%);border-radius:60% 40% 0 0/40px 30px 0 0}

/* front */
.splash{position:absolute;left:30px;top:105px;width:460px;height:470px}
.headline{position:absolute;left:95px;top:250px;width:350px;color:#fff;font-family:"Montserrat",sans-serif;font-weight:800;text-transform:uppercase}
.headline__small{display:block;font-size:36px;line-height:42px;letter-spacing:1px}
.headline__rule{display:block;border-top:3px dotted #fff;margin:8px 0 6px;width:335px}
.headline__big{display:block;font-size:55px;line-height:58px;letter-spacing:2px}

.claim{position:absolute;right:0;background:var(--lime);color:var(--navy);border-radius:14px 0 0 14px;box-shadow:2px 3px 0 var(--lime-dark)}
.claim--protein{top:538px;width:388px;height:60px;padding:8px 0 0 22px}
.claim--protein strong{display:block;font-size:15.5px;font-weight:700;line-height:21px}
.claim--protein span{display:block;font-size:15px;line-height:22px}
.claim--free{top:612px;width:330px;height:62px;padding:8px 0 0 30px;font-size:18px;line-height:24px}

.pack-foot{position:absolute;left:90px;top:680px;display:flex;align-items:center;gap:10px}
.pack-foot__weight{font-size:17px;color:var(--teal-dark)}
.pack-foot__divider{width:1px;height:30px;background:var(--rule)}
.brand-name{font-family:"Open Sans",sans-serif;font-weight:400;color:var(--brand)}
.pack-foot .brand-name{font-size:27px}
.badge{width:52px;height:34px;background:var(--brand);border-radius:3px}

/* back */
.back-title{position:absolute;left:20px;top:160px;width:480px;font-family:"Montserrat",sans-serif;font-weight:800;text-transform:uppercase;color:var(--teal-dark)}
.back-title__small{display:block;font-size:27px;letter-spacing:1px;line-height:32px;color:var(--teal)}
.back-title__big{display:block;font-size:37px;letter-spacing:1.5px;line-height:42px}

.info{position:absolute;left:22px;top:262px;width:228px;font-size:11.6px;line-height:14.6px}
.info__block{margin-bottom:14px}
.info__label{display:flex;align-items:center;gap:5px;font-weight:700;color:var(--teal-dark);font-size:12px;margin-bottom:3px}
.info__label svg{width:14px;height:6px}
.info__inline{font-weight:400;color:var(--teal);font-size:13px}
.info p{text-align:justify}
.info__weight{font-weight:700;color:var(--teal-dark);font-size:13px;margin-top:6px}

.nutrition{position:absolute;left:268px;top:262px;width:224px;border:2px solid var(--rule);font-family:"Roboto Condensed",sans-serif;font-size:10px;color:#5d6669}
.nutrition__head{padding:5px 6px;border-bottom:2px solid var(--rule);font-size:10.5px}
.nutrition__head small{font-size:8px}
.nutrition table{width:100%;border-collapse:collapse}
.nutrition td{padding:4px 6px;border-bottom:1px solid #c7cdcf;vertical-align:top}
.nutrition td:last-child{text-align:right;font-size:8.5px}
.nutrition__free{padding:5px 6px;font-size:9.5px;line-height:12px}

.back-brand{position:absolute;left:268px;top:535px;width:224px;text-align:center}
.back-brand .brand-name{font-size:32px;display:block}
.follow{display:flex;justify-content:center;align-items:center;gap:10px;margin-top:2px;font-family:"Roboto Condensed",sans-serif;font-weight:700;color:var(--teal-dark)}
.follow__text{font-size:15px}
.follow__tag{font-size:10px}
</style>
</head>
<body>

<section class="pack pack--front" aria-label="Pack front">
  <div class="coral-band" role="img" aria-label="Watercolour coral and seaweed illustration"></div>

  <svg class="splash" viewBox="0 0 460 470" role="img" aria-label="Blue watercolour splash with sea map and fish illustration">
    <defs>
      <linearGradient id="splashFill" x1="0" y1="0" x2="1" y2="1">
        <stop offset="0" stop-color="#5cc3cf"/>
        <stop offset="0.6" stop-color="#2a9db2"/>
        <stop offset="1" stop-color="#1d7f93"/>
      </linearGradient>
    </defs>
    <path fill="url(#splashFill)" d="M40 30 C120 10 180 40 220 110 C260 40 330 10 420 35 C450 120 440 200 410 250 C450 300 440 380 400 440 C300 470 140 470 40 440 C10 380 5 310 30 250 C0 190 5 100 40 30 Z"/>
  </svg>

  <h1 class="headline">
    <span class="headline__small">Wild Marine</span>
    <span class="headline__small">Hydrolized</span>
    <span class="headline__rule"></span>
    <span class="headline__big">Collagen</span>
    <span class="headline__big">Powder</span>
  </h1>

  <div class="claim claim--protein">
    <strong>Essential Protein for Muscle, Hair and Skin</strong>
    <span>High in Amino Acids | Sustainably Sourced</span>
  </div>
  <div class="claim claim--free">Gluten Free | No Additives |<br>Unflavoured and Water-Soluble</div>

  <div class="pack-foot">
    <span class="pack-foot__weight">200G</span>
    <span class="pack-foot__divider"></span>
    <span class="brand-name">Pramuvents</span>
    <span class="badge" aria-label="KWR certification badge"></span>
  </div>

  <div class="wave-band" role="img" aria-label="Illustrated ocean waves and seaweed"></div>
</section>

<section class="pack pack--back" aria-label="Pack back">
  <div class="coral-band" role="img" aria-label="Watercolour coral and seaweed illustration"></div>

  <h2 class="back-title">
    <span class="back-title__small">Wild Marine&nbsp; Hydrolized</span>
    <span class="back-title__big">Collagen Powder</span>
  </h2>

  <div class="info">
    <div class="info__block">
      <div class="info__label">Servering <svg viewBox="0 0 14 6"><ellipse cx="7" cy="3" rx="7" ry="2.6" fill="currentColor"/></svg> <span class="info__inline">1-2 teaspoon</span></div>
    </div>
    <div class="info__block">
      <div class="info__label">Indredients <svg viewBox="0 0 14 6"><ellipse cx="7" cy="3" rx="7" ry="2.6" fill="currentColor"/></svg></div>
      <p>100% Pure Hydrolysed Marine Collagen (Natural) Derived from Fish</p>
    </div>
    <div class="info__block">
      <div class="info__label">Caution <svg viewBox="0 0 14 6"><ellipse cx="7" cy="3" rx="7" ry="2.6" fill="currentColor"/></svg></div>
      <p>This supplement should not be used as a substitute for a varied diet Do not exceed the recommended daily dose. Please consult a healthcare practitioner if you are pregnant or taking prescription medicine before using this product.</p>
    </div>
    <div class="info__block">
      <div class="info__label">Storage <svg viewBox="0 0 14 6"><ellipse cx="7" cy="3" rx="7" ry="2.6" fill="currentColor"/></svg></div>
      <p>Store in a cool dry place away from sunlight, moisture, and heat. Keep out of reach of animals and children. Keep contents dry. Reject if pack seal is broken.</p>
    </div>
    <div class="info__weight">NEW WT. 200G</div>
  </div>

  <div class="nutrition">
    <div class="nutrition__head">Nutritional Information: <small>Typical Values Per 10g Serving</small></div>
    <table>
      <tr><td>Energy</td><td>159Kj/38kCal</td></tr>
      <tr><td>Protein</td><td>9.5g</td></tr>
      <tr><td>Carbohydrates</td><td>0.02g</td></tr>
      <tr><td>Of which sugars</td><td>0.02g</td></tr>
      <tr><td>Amino Acids<br>Of which essential</td><td>99.9%<br>14.5%</td></tr>
      <tr><td>Fat</td><td>0g</td></tr>
      <tr><td>Fibre</td><td>0g</td></tr>
      <tr><td>Sodium</td><td>0g</td></tr>
    </table>
    <div class="nutrition__free">Free from GMO, Fat, Carbohydrates, Purine, Preservatives, Artificial colours/flavours</div>
  </div>

  <div class="back-brand">
    <span class="brand-name">Pramuvents</span>
    <div class="follow"><span class="follow__text">Follow us!</span><span class="follow__tag">#Pramuvents</span></div>
  </div>

  <div class="wave-band" style="height:100px" role="img" aria-label="Illustrated fish, seaweed and ocean waves"></div>
</section>

</body>
</html>
```